Net Clarity Partners Needs a New Business Card Design

Attached is my new logo that ArtFlockly created and picture of me for the back of the business card. Also attached is the information to include on the business card (on my existing business card design - NCP1 file attached).

The designer also provided a treatment of my logo that I really like if you can use it somehow. Also attached - file name "Preferred Version of New Logo."

Marla Quinteros

Net Clarity Partners
4817 Brindle Ave., #315
Houston, TX 77056

Tel: (832) 555-0147
www.netclaritypartners.example
marla@netclaritypartners.example

Thank you.

Target Market(s)

attorneys and law firms

Industry/Entity Type

Legal

Contact Information for Business Card

Proved in the Project Description

Font styles to use
Other font styles liked:
• I am open on font - no script though.

Colors
2d73b3
33a6d7

Requirements
Must have
• my logo
• company name & contact info
• my picture on the back
• colors that coordinate with the logo
Nice to have
• love to use the treated version of the logo if possible

```html
<!DOCTYPE html>
<html lang="en">
<head>
<meta charset="utf-8">
<title>Net Clarity Partners — Business Card</title>
<link rel="stylesheet" href="https://fonts.googleapis.com/css2?family=Open+Sans:wght@400;600&display=swap">
<style>
  :root {
    --backdrop: #173a4b;
    --card-white: #ffffff;
    --card-dark: #26333b;
    --brand-blue: #29a4dc;
    --brand-grey: #6f7275;
    --text-light: #ffffff;
    --photo-top: #d9c3a8;
    --photo-bottom: #3a3fa0;
  }
  * { box-sizing: border-box; margin: 0; padding: 0; }
  html, body {
    width: 1200px; height: 800px; overflow: hidden;
    background: var(--backdrop);
    font-family: "Open Sans", Arial, sans-serif;
  }
  .canvas {
    position: relative; width: 1200px; height: 800px;
    display: flex; align-items: center; justify-content: center; gap: 60px;
  }
  .card {
    position: relative; width: 525px; height: 300px; overflow: hidden;
    box-shadow: 0 12px 30px rgba(0,0,0,0.35);
  }
  /* Front: brand and portrait */
  .card-front { background: var(--card-white); }
  .brand-block { position: absolute; left: 32px; top: 40px; }
  .brand-lockup { display: flex; align-items: center; gap: 10px; }
  .brand-square { width: 16px; height: 16px; background: var(--brand-blue); flex: none; }
  .brand-name {
    font-size: 22px; font-weight: 600; color: var(--brand-blue);
    letter-spacing: 0.5px; text-transform: uppercase; white-space: nowrap;
  }
  .tagline {
    margin-top: 4px; margin-left: 26px;
    font-size: 9px; letter-spacing: 3px; color: var(--brand-grey);
    text-transform: uppercase; white-space: nowrap;
  }
  .portrait {
    position: absolute; right: 50px; bottom: 0;
    width: 210px; height: 185px;
    border-radius: 100px 100px 0 0;
    background: linear-gradient(180deg, var(--photo-top) 0%, var(--photo-top) 45%, var(--photo-bottom) 75%);
  }
  /* Back: contact details */
  .card-back { background: var(--card-dark); color: var(--text-light); }
  .contact { position: absolute; left: 40px; top: 38px; }
  .person-name {
    font-size: 22px; font-weight: 600; color: var(--brand-blue);
    text-transform: uppercase; letter-spacing: 1px;
  }
  .person-title { font-size: 14px; margin-top: 2px; }
  .details { margin-top: 26px; font-size: 14px; line-height: 1.45; font-style: normal; }
  .details .company { color: var(--brand-blue); }
  .back-mark {
    position: absolute; right: 36px; bottom: 44px;
    display: flex; align-items: center; gap: 8px;
  }
  .back-mark .brand-square { width: 14px; height: 14px; }
  .back-mark .brand-name { font-size: 18px; }
</style>
</head>
<body>
  <main class="canvas">
    <section class="card card-front" aria-label="Business card front">
      <div class="brand-block">
        <div class="brand-lockup">
          <span class="brand-square"></span>
          <span class="brand-name">Net Clarity Partners</span>
        </div>
        <p class="tagline">Smart marketing for law firms</p>
      </div>
      <div class="portrait" role="img" aria-label="Portrait photo of Marla Quinteros"></div>
    </section>

    <section class="card card-back" aria-label="Business card back">
      <div class="contact">
        <h1 class="person-name">Marla Quinteros</h1>
        <p class="person-title">Founder</p>
        <address class="details">
          <span class="company">Net Clarity Partners</span><br>
          4817 Brindle Ave., #315<br>
          Houston, TX 77056<br>
          Tel: (832) 555-0147<br>
          www.netclaritypartners.example
        </address>
      </div>
      <div class="back-mark">
        <span class="brand-square"></span>
        <span class="brand-name">Net Clarity Partners</span>
      </div>
    </section>
  </main>
</body>
</html>
```